Business Card Design Project

I am a Chiropractor that is looking for a new business card.  Our logo was slightly changed lately, therefore need a new, more professional look.
We are a modern, non-stuffy chiropractic office.  Want a contemporary look that will let people know this is not your typical doctors office.  Our logo is red, and contains the name of our business: realign.  The u in the logo is green, stressing the most important part of our business: "u"

Target Market(s)
moderate to upper income bracket, family friendly
www.realignspine.example
Gordon Pell
Family Chiropractor
412 Birch Ave
Alder Creek, TX 78990
512.555.0147 phone
512.555.0148 fax
Industry/Entity Type
Business
Requirements
Must have
- www.realignspine.example
Gordon Pell
Family Chiropractor
412 Birch Ave
Alder Creek, TX 78990
512.555.0147 phone
512.555.0148 fax

```html
<!DOCTYPE html>
<html lang="en">
<head>
<meta charset="utf-8">
<title>realign — Business Card</title>
<link rel="stylesheet" href="https://fonts.googleapis.com/css2?family=Source+Sans+3:wght@400;600;700&display=swap">
<style>
  :root {
    --paper: #ffffff;
    --card-red: #fe1e22;
    --card-green: #66ff12;
    --ink-light: #ffffff;
    --accent-red: #ee1f2a;
  }
  html, body {
    margin: 0;
    padding: 0;
    width: 1200px;
    height: 717px;
    overflow: hidden;
    background: var(--paper);
  }
  .canvas {
    position: relative;
    width: 1200px;
    height: 717px;
    font-family: "Source Sans 3", "Myriad Pro", sans-serif;
  }
  .card {
    position: absolute;
    left: 19px;
    top: 16px;
    width: 1159px;
    height: 671px;
    border-radius: 88px;
    overflow: hidden;
    display: flex;
  }
  .card__contact {
    width: 691px;
    height: 100%;
    background: var(--card-red);
    color: var(--ink-light);
    position: relative;
    text-align: center;
  }
  .card__brand {
    flex: 1;
    background: var(--card-green);
    position: relative;
  }
  .contact__line {
    position: absolute;
    left: 0;
    width: 690px;
    margin: 0;
    font-size: 31px;
    line-height: 1;
    letter-spacing: 0.3px;
  }
  .contact__name { top: 101px; font-weight: 700; }
  .contact__title { top: 143px; font-weight: 400; }
  .contact__web { top: 319px; }
  .contact__address { top: 453px; }
  .contact__city { top: 495px; }
  .contact__phone { top: 534px; }
  .contact__fax { top: 573px; }

  .brand__mark {
    position: absolute;
    left: 0;
    right: 0;
    top: 290px;
    display: flex;
    align-items: center;
    justify-content: center;
    gap: 16px;
  }
  .brand__dot {
    width: 22px;
    height: 22px;
    border-radius: 50%;
    background: var(--accent-red);
  }
  .brand__name {
    font-size: 70px;
    font-weight: 400;
    line-height: 1;
    color: var(--accent-red);
    letter-spacing: 1px;
  }
</style>
</head>
<body>
  <main class="canvas">
    <section class="card">
      <div class="card__contact">
        <p class="contact__line contact__name">Gordon Pell</p>
        <p class="contact__line contact__title">Family Chiropractor</p>
        <p class="contact__line contact__web">www.realignspine.example</p>
        <p class="contact__line contact__address">412 Birch Ave</p>
        <p class="contact__line contact__city">Alder Creek, TX 78990</p>
        <p class="contact__line contact__phone">Phone: 512.555.0147</p>
        <p class="contact__line contact__fax">Fax: 512.555.0148</p>
      </div>
      <div class="card__brand">
        <div class="brand__mark">
          <span class="brand__dot"></span>
          <span class="brand__name">realign</span>
        </div>
      </div>
    </section>
  </main>
</body>
</html>
```